Template design for an Online "Membership Subscription" System

I need a template for a service that will allow website owners to create their own online subscription services and member portals.
With just a snippet of code they can password protect certain parts of their website.
Tagline:
"Monetize your website with TallowGateHubs"
"The Easiest Way To Turn Your Website Into 'Members Only'"
Call to action "Try For Free" and "Watch a demo"
Features:
1. Quick & easy to set up
2. Works with any website
3. Charge one-time or subscription fees
4. Automated billing, sign up and more
5. Customize to match your website
6. Unlimited members
Similar websites/services;
https://quillhavenvault.example
https://joinbrook.example
https://www.clubnestly.example
I'd like a clean looking, uncluttered design targeted towards "non-techie" people. Easy to read without a lot going on. Emphasizing ease of use and pushing towards a "Try for free" option.
Separate into sections with the top section having the tagline. Followed by feature overview, testimonials, sample use cases.
A footer with multiple links by industry that can provide a case study for various use cases;
Ex;
Clubs
Religious Organizations
Online Stores
Digital Products
Education
Coaching
Fitness
Target Market(s)
Non technical small business owners
Number of Pages Required
2 page
Look and feel

```html
<!DOCTYPE html>
<html lang="en">
<head>
<meta charset="UTF-8">
<title>TallowGateHubs – Membership Platform</title>
<link href="https://fonts.googleapis.com/css2?family=Montserrat:wght@300;400;500&family=Signika:wght@400;500;600&display=swap" rel="stylesheet">
<style>
:root{
  --navy:#0a1440;
  --navy-deep:#08112f;
  --royal:#0a52a5;
  --accent:#0e63b8;
  --cta:#1a8fd8;
  --mist:#e6edf7;
  --ink:#2b2f3a;
  --white:#ffffff;
  --card-line:#4a78c2;
}
*{margin:0;padding:0;box-sizing:border-box}
html,body{width:1200px;height:3155px;overflow:hidden}
body{position:relative;font-family:'Montserrat',sans-serif;color:var(--ink);background:var(--white)}
.abs{position:absolute}
.heading{font-family:'Signika',sans-serif}

/* hero */
.hero{position:absolute;left:0;top:0;width:1200px;height:640px;background:var(--navy)}
.hero-wave{position:absolute;left:0;top:540px}
.brand{position:absolute;font-family:'Signika',sans-serif;font-weight:600;color:var(--white);font-size:21px;letter-spacing:.3px}
.nav a{position:absolute;top:44px;color:var(--white);font-size:15px;font-weight:400;text-decoration:none;transform:translateX(-50%)}
.nav .active{border:1px solid var(--white);padding:2px 20px}
.hero-title{left:120px;top:236px;width:460px;font-family:'Signika',sans-serif;font-weight:500;color:var(--white);font-size:31px;line-height:40px}
.btn{position:absolute;display:flex;align-items:center;justify-content:center;width:152px;height:40px;background:var(--cta);color:var(--white);font-size:15.5px;font-weight:400;text-decoration:none}
.hero-art{left:612px;top:171px;width:490px;height:331px;border-radius:30px;background:radial-gradient(ellipse at 60% 55%,#3a3ad6 0%,#1d2a8a 40%,rgba(10,20,64,0) 75%)}

/* sections */
.about{position:absolute;left:0;top:640px;width:1200px;height:410px;background:var(--mist)}
.features{position:absolute;left:0;top:1050px;width:1200px;height:686px;background:var(--white)}
.cases{position:absolute;left:0;top:1736px;width:1200px;height:465px;background:var(--royal)}
.dots{position:absolute;transform:translateX(-50%)}
.section-title{position:absolute;transform:translateX(-50%);font-family:'Signika',sans-serif;font-weight:600;color:var(--accent);white-space:nowrap}
.body-copy{position:absolute;font-size:16px;line-height:27.2px;font-weight:300;text-align:justify}
.about-photo{left:778px;top:716px;width:333px;height:264px;border-radius:0 70px 100px 0;background:linear-gradient(135deg,#d9dde4,#aab3c2 55%,#c44a4f)}
.about-bar{left:758px;top:961px;width:260px;height:39px;background:var(--accent);border-radius:4px}

.feature{position:absolute;width:240px;transform:translateX(-50%);text-align:center}
.feature .icon{width:86px;height:86px;border-radius:50%;margin:0 auto;background:linear-gradient(135deg,#eef1f6,#d8dee9)}
.feature p{font-size:16.5px;line-height:24px;margin-top:40px;color:#222}

.case-img{position:absolute;top:1891px;width:201px;height:236px;border:2px solid var(--white);border-radius:8px}

/* testimonials */
.card{position:absolute;top:2395px;width:277px;height:277px;border:1px solid var(--card-line);background:var(--white)}
.card .quote{position:absolute;left:16px;right:16px;top:36px;font-size:11.2px;line-height:20px;text-align:justify;color:#333}
.card .mark{position:absolute;left:50%;top:86px;transform:translateX(-50%);font-family:'Signika',sans-serif;font-size:120px;line-height:1;color:rgba(70,140,210,.25)}
.card .name{position:absolute;left:0;right:0;top:194px;text-align:center;font-family:'Signika',sans-serif;font-weight:600;font-size:16px;color:#111}
.card .place{position:absolute;left:0;right:0;top:222px;text-align:center;font-size:15px;color:#111}
.card .tail{position:absolute;left:196px;top:275px}
.arrow{position:absolute;top:2518px}

/* footer */
.footer{position:absolute;left:0;top:2760px;width:1200px;height:326px;background:var(--royal)}
.footer-wave{position:absolute;left:0;top:2750px}
.foot-col h4{font-family:'Signika',sans-serif;font-weight:600;color:var(--white);font-size:16px;margin-bottom:8px}
.foot-col a{display:block;color:var(--white);font-size:14px;line-height:24px;text-decoration:none;font-weight:400}
.social span{display:inline-block;width:13px;height:13px;border:2px solid var(--white);border-radius:50%;margin-right:14px}
.news-input{left:812px;top:2895px;width:180px;height:44px;background:var(--white);color:#aab;font-size:14px;padding:13px 14px}
.news-submit{left:996px;top:2895px;width:78px;height:44px;background:var(--cta);color:var(--white);font-size:15px;display:flex;align-items:center;justify-content:center}
.bottom-bar{position:absolute;left:0;top:3086px;width:1200px;height:69px;background:var(--navy);color:var(--white);font-size:12.5px;font-weight:500;text-align:center;padding-top:17px}
</style>
</head>
<body>

<header class="hero">
  <div class="brand" style="left:120px;top:43px">TALLOWGATEHUBS</div>
  <nav class="nav">
    <a class="active" href="#" style="left:616px;top:41px">Home</a>
    <a href="#" style="left:719px">Features</a>
    <a href="#" style="left:840px">Testimonial</a>
    <a href="#" style="left:953px">Cases</a>
    <a href="#" style="left:1051px">Contact</a>
  </nav>
  <h1 class="abs hero-title">"Monetize your website with TallowGateHubs"<br>"The Easiest Way To Turn Your Website Into 'Members Only'"</h1>
  <a class="btn" href="#" style="left:120px;top:423px">Get Started</a>
  <div class="abs hero-art" role="img" aria-label="Isometric illustration of a laptop, phone and tablet showing dashboards and charts"></div>
</header>
<svg class="hero-wave" width="1200" height="100" viewBox="0 0 1200 100">
  <path d="M0 78 C150 40 300 30 450 38 C650 48 900 70 1200 90 L1200 100 L0 100Z" fill="#e6edf7"/>
</svg>

<section class="about">
  <svg class="dots" style="left:600px;top:44px" width="50" height="18" viewBox="0 0 50 18">
    <circle cx="10" cy="9" r="8" fill="#0a52a5"/><circle cx="25" cy="9" r="8" fill="#1a6fd0"/><circle cx="40" cy="9" r="8" fill="#0a52a5"/>
  </svg>
  <h2 class="section-title" style="left:600px;top:72px;font-size:29px">About Us</h2>
  <p class="body-copy" style="left:120px;top:128px;width:606px">Lorem ipsum dolor sit amet, consectetur adipiscing elit, sed do eiusmod tempor incididunt ut labore et dolore magna aliqua. Quis ipsum suspendisse ultrices gravida. Risus commodo viverra maecenas accumsan lacus vel facilisis. Lorem ipsum dolor sit amet, consectetur adipiscing elit, sed do eiusmod tempor incididunt ut labore et dolore magna aliqua. Quis ipsum suspendisse ultrices gravida.</p>
  <a class="btn" href="#" style="left:120px;top:291px">Read More</a>
</section>
<div class="abs about-bar"></div>
<div class="abs about-photo" role="img" aria-label="Photo of a small team working together at computers in an office"></div>

<section class="features">
  <svg class="dots" style="left:600px;top:78px" width="50" height="18" viewBox="0 0 50 18">
    <circle cx="10" cy="9" r="8" fill="#0a52a5"/><circle cx="25" cy="9" r="8" fill="#1a6fd0"/><circle cx="40" cy="9" r="8" fill="#0a52a5"/>
  </svg>
  <h2 class="section-title" style="left:600px;top:100px;font-size:38px">Features</h2>
  <div class="feature" style="left:190px;top:186px"><div class="icon" role="img" aria-label="Icon: tools with easy to install label"></div><p>Quick &amp; Easy<br>To Set Up</p></div>
  <div class="feature" style="left:458px;top:186px"><div class="icon" role="img" aria-label="Icon: browser window with cursor"></div><p>Works With<br>Any Website</p></div>
  <div class="feature" style="left:726px;top:186px"><div class="icon" role="img" aria-label="Icon: hand holding a phone with payment screens"></div><p>Charge One-Time<br>Or Subscription Fees</p></div>
  <div class="feature" style="left:987px;top:186px"><div class="icon" role="img" aria-label="Icon: billing document and sign up form"></div><p>Automated Billing,<br>Sign Up And More</p></div>
  <div class="feature" style="left:454px;top:440px"><div class="icon" role="img" aria-label="Icon: customizable web layout"></div><p>Customize To Match<br>Your Website</p></div>
  <div class="feature" style="left:736px;top:440px"><div class="icon" role="img" aria-label="Icon: group of members"></div><p>Unlimited<br>Members</p></div>
</section>

<section class="cases">
  <svg class="dots" style="left:600px;top:50px" width="50" height="18" viewBox="0 0 50 18">
    <circle cx="10" cy="9" r="8" fill="#ffffff"/><circle cx="25" cy="9" r="8" fill="#dbe6f5"/><circle cx="40" cy="9" r="8" fill="#ffffff"/>
  </svg>
  <h2 class="section-title" style="left:600px;top:78px;font-size:30px;color:#fff;font-weight:500">Cases</h2>
  <p class="body-copy" style="left:120px;top:156px;width:496px;color:#fff;font-weight:400">Lorem ipsum dolor sit amet, consectetur adipiscing elit, sed do eiusmod tempor incididunt ut labore et dolore magna aliqua. Quis ipsum suspendisse ultrices gravida. Risus commodo viverra maecenas accumsan lacus vel facilisis. Lorem ipsum dolor sit amet, consectetur adipiscing elit, sed do eiusmod tempor incididunt ut labore et dolore magna aliqua.</p>
  <a class="btn" href="#" style="left:120px;top:339px">View Cases</a>
</section>
<div class="case-img" style="left:656px;background:linear-gradient(135deg,#0e9fb8,#0b3a7a 55%,#e04a8a)" role="img" aria-label="Illustration of software coding and testing on a laptop"></div>
<div class="case-img" style="left:876px;background:linear-gradient(135deg,#1c3d78,#0a1d45 60%,#2a64b0)" role="img" aria-label="Photo of hands typing on a laptop with task progress overlays"></div>

<section>
  <svg class="dots" style="left:596px;top:2259px" width="50" height="18" viewBox="0 0 50 18">
    <circle cx="10" cy="9" r="8" fill="#0a52a5"/><circle cx="25" cy="9" r="8" fill="#1a6fd0"/><circle cx="40" cy="9" r="8" fill="#0a52a5"/>
  </svg>
  <h2 class="section-title" style="left:595px;top:2283px;font-size:29px">Testimonials</h2>
  <p class="abs" style="left:0;width:1190px;top:2332px;text-align:center;font-size:16px;font-weight:300">Lorem ipsum dolor sit amet, consectetur adipiscing elit, sed do eiusmod tempor incididunt ut labore et dolore magna aliqua.</p>

  <svg class="arrow" style="left:104px" width="18" height="26" viewBox="0 0 18 26"><path d="M14 3 L4 13 L14 23" stroke="#111" stroke-width="3" fill="none"/></svg>
  <svg class="arrow" style="left:1078px" width="18" height="26" viewBox="0 0 18 26"><path d="M4 3 L14 13 L4 23" stroke="#111" stroke-width="3" fill="none"/></svg>

  <article class="card" style="left:147px">
    <div class="mark">“</div>
    <p class="quote">Lorem ipsum dolor sit amet, consectetur adipiscing elit, sed do eiusmod tempor incididunt ut labore et dolore magna aliqua. Ut enim ad minim veniam, quis nostrud exercitation ullamco laboris nisi ut aliquip ex ea commodo consequat. Duis aute irure dolor in reprehenderit in voluptate</p>
    <div class="name">Dana Whitlow</div><div class="place">USA</div>
    <svg class="tail" width="24" height="22" viewBox="0 0 24 22"><path d="M0 0 L0 21 L23 0" fill="#fff" stroke="#4a78c2" stroke-width="1"/></svg>
  </article>
  <article class="card" style="left:464px">
    <div class="mark">“</div>
    <p class="quote">Lorem ipsum dolor sit amet, consectetur adipiscing elit, sed do eiusmod tempor incididunt ut labore et dolore magna aliqua. Ut enim ad minim veniam, quis nostrud exercitation ullamco laboris nisi ut aliquip ex ea commodo consequat. Duis aute irure dolor in reprehenderit in voluptate</p>
    <div class="name">Dana Whitlow</div><div class="place">USA</div>
    <svg class="tail" width="24" height="22" viewBox="0 0 24 22"><path d="M0 0 L0 21 L23 0" fill="#fff" stroke="#4a78c2" stroke-width="1"/></svg>
  </article>
  <article class="card" style="left:781px">
    <div class="mark">“</div>
    <p class="quote">Lorem ipsum dolor sit amet, consectetur adipiscing elit, sed do eiusmod tempor incididunt ut labore et dolore magna aliqua. Ut enim ad minim veniam, quis nostrud exercitation ullamco laboris nisi ut aliquip ex ea commodo consequat.</p>
    <div class="name">Dana Whitlow</div><div class="place">USA</div>
    <svg class="tail" width="24" height="22" viewBox="0 0 24 22"><path d="M0 0 L0 21 L23 0" fill="#fff" stroke="#4a78c2" stroke-width="1"/></svg>
  </article>
</section>

<footer>
  <div class="footer"></div>
  <svg class="footer-wave" width="1200" height="60" viewBox="0 0 1200 60">
    <path d="M0 0 L1200 0 L1200 56 C1000 36 800 20 600 18 C400 16 200 22 0 42Z" fill="#ffffff"/>
  </svg>
  <div class="brand" style="left:122px;top:2858px">TALLOWGATEHUBS</div>
  <div class="abs social" style="left:120px;top:2911px"><span></span><span></span><span></span></div>
  <div class="abs foot-col" style="left:415px;top:2858px">
    <h4>Quick Links</h4>
    <a href="#">Home</a><a href="#">About Us</a><a href="#">Feature</a><a href="#">Testimonial</a><a href="#">Cases</a><a href="#">Contacts</a>
  </div>
  <div class="abs foot-col" style="left:602px;top:2858px">
    <h4>Help Links</h4>
    <a href="#">Clubs</a><a href="#">Religious Organizations</a><a href="#">Online Stores</a><a href="#">Digital Products</a><a href="#">Education</a><a href="#">Coaching</a><a href="#">Fitness</a>
  </div>
  <div class="abs foot-col" style="left:812px;top:2858px"><h4>Join Our Newletter</h4></div>
  <div class="abs news-input">Email</div>
  <div class="abs news-submit">Submit</div>
  <div class="bottom-bar">© copyrights 2022 TallowGateHubs | &nbsp;All Rights Reserved</div>
</footer>

</body>
</html>
```